Home web page re-vamp

I would like a stylish new home page design for a clients website.
I have included a sitemap to give some guidance.
The site needs to show off the design capabilitiesof the client

```html
<!DOCTYPE html>
<html lang="en">
<head>
<meta charset="utf-8">
<title>Your Company Name – Architects &amp; Designers</title>
<link rel="stylesheet" href="https://fonts.googleapis.com/css2?family=PT+Sans+Narrow:wght@400;700&family=PT+Sans:wght@400;700&display=swap">
<style>
:root{
  --topbar:#3f5f8e;
  --navy:#0e2a66;
  --royal:#1241a8;
  --heading:#1f4a8c;
  --ink:#2b2b2b;
  --muted:#4a4a4a;
  --paper:#f2efe8;
  --card:#fafafa;
  --green:#93bf35;
  --green-text:#8ab42c;
  --footer:#444444;
  --white:#ffffff;
  --frame:#7b9be0;
}
*{box-sizing:border-box;margin:0;padding:0}
html,body{width:741px;height:1200px;overflow:hidden}
body{font-family:"PT Sans",Arial,sans-serif;background:var(--paper);color:var(--ink)}
.page{position:relative;width:741px;height:1200px;overflow:hidden;background:var(--paper)}
.abs{position:absolute}
.narrow{font-family:"PT Sans Narrow","Arial Narrow",sans-serif}

/* header */
.topbar{left:0;top:0;width:741px;height:17px;background:var(--topbar);color:var(--white);font-size:8px;text-align:right;padding:4px 85px 0 0}
.navbar{left:0;top:17px;width:741px;height:31px;background:rgba(255,255,255,.93)}
.logo-box{left:62px;top:0;width:158px;height:48px;background:var(--white);color:var(--heading);font-weight:700;font-size:16px;letter-spacing:.5px;padding:17px 0 0 25px}
.main-nav{top:28px;left:253px;display:flex;gap:0;font-size:8px;color:var(--heading)}
.main-nav span{margin-right:21px}

/* hero */
.hero{left:0;top:48px;width:741px;height:338px;background:linear-gradient(180deg,#6f7f95 0%,#a9b5c2 45%,#c9cfc9 62%,#6f8a4e 75%,#4d6b30 100%)}
.hero-screen{left:202px;top:88px;width:367px;height:224px;border:3px solid #3a3f47;border-radius:14px;background:linear-gradient(180deg,#9fb0c7 0%,#b7c3d2 50%,#5f7d45 85%)}
.hero-band{left:202px;top:167px;width:367px;height:115px;background:rgba(56,86,140,.55)}
.hero-title{left:202px;top:189px;width:367px;text-align:center;color:var(--white);font-size:19px;font-weight:700}
.hero-sub{left:202px;top:216px;width:367px;text-align:center;color:var(--white);font-size:13.5px}
.hero-btn{left:250px;top:245px;width:265px;height:28px;background:var(--white);border:3px solid var(--heading);color:var(--heading);font-size:14px;text-align:center;line-height:22px}

/* feature cards */
.card{top:338px;width:134px;height:224px;background:var(--card)}
.card-img{position:absolute;left:10px;top:10px;width:114px;height:87px}
.card-title{position:absolute;left:0;top:108px;width:100%;text-align:center;font-size:18.5px;line-height:22px;color:#333}
.card-text{position:absolute;left:12px;top:163px;width:115px;font-size:11.5px;line-height:15px;color:var(--muted)}
.card-arrow{position:absolute;right:10px;bottom:7px}
.why{left:81px;top:338px;width:135px;height:455px}
.why .card-img{border:2px solid var(--white);left:10px;width:116px}
.why-title{left:81px;top:446px;width:135px;text-align:center;color:var(--white);font-size:18.5px;line-height:22px}
.why-text{left:103px;top:501px;width:105px;color:var(--white);font-size:12px;line-height:15px}

/* project band */
.band{left:0;top:569px;width:741px;height:255px;background:var(--royal)}
.checks{left:86px;top:577px;width:130px;color:var(--white);font-size:9.5px;line-height:11.5px;list-style:none}
.checks li{position:relative;padding-left:15px;margin-bottom:12px}
.checks svg{position:absolute;left:1px;top:2px}
.project-title{left:248px;top:590px;color:var(--white);font-size:18px}
.project-name{left:249px;top:634px;color:var(--white);font-size:9.5px;font-weight:700}
.project-text{left:248px;top:652px;width:150px;color:var(--white);font-size:9.5px;line-height:12px}
.project-text p{margin-bottom:11px}
.project-img{left:410px;top:586px;width:248px;height:226px;border:4px solid var(--frame);border-radius:3px;background:linear-gradient(160deg,#0f3f5c 0%,#1a6f96 45%,#3fb2d8 70%,#0b2c45 100%)}
.dot{top:791px;width:10px;height:10px;border-radius:50%;background:var(--white)}

/* testimonial + news */
.section-title{color:var(--heading);font-size:18px}
.slider-arrows{left:402px;top:855px;color:var(--heading);font-size:17px;word-spacing:16px}
.quote{left:98px;top:891px;width:353px;height:107px;background:var(--green);border-radius:14px}
.quote-text{left:147px;top:912px;width:290px;color:var(--white);font-size:13.5px;line-height:18px}
.quote-client{left:147px;top:958px;color:#eaf4d3;font-size:11px;line-height:14px}
.news-date{left:484px;top:893px;color:var(--green-text);font-size:11px;font-weight:700}
.news-text{left:483px;top:914px;width:185px;font-size:9.5px;line-height:12px;color:var(--ink)}
.read-more{left:483px;top:976px;font-size:9.5px;font-weight:700;color:var(--ink)}
.call{left:0;top:1010px;width:741px;text-align:center;color:var(--heading);font-size:30.5px;font-weight:700}

/* footer */
.footer-line{left:0;top:1054px;width:741px;height:6px;background:var(--royal)}
.footer{left:0;top:1060px;width:741px;height:96px;background:var(--footer)}
.footer-nav{left:155px;top:1081px;color:var(--white);font-size:8px;display:flex}
.footer-nav span{margin-right:30px}
.social{left:311px;top:1112px;display:flex;gap:4px}
.copyright{left:0;top:1166px;width:741px;text-align:center;color:var(--ink);font-size:11px}
</style>
</head>
<body>
<div class="page">

  <div class="abs topbar">Call Us Now 1123 456 789</div>
  <div class="abs navbar"></div>
  <div class="abs logo-box">YOUR LOGO</div>
  <nav class="abs main-nav">
    <span>About Us</span><span>Services</span><span>Our Clients</span><span>Gallery</span><span>Healty &amp; Safety</span><span>Specification Sheets</span><span>Contact Us</span>
  </nav>

  <div class="abs hero" role="img" aria-label="Photo of two hands holding a tablet framing a wireframe building over a green field and cloudy sky"></div>
  <div class="abs hero-screen"></div>
  <div class="abs hero-band"></div>
  <div class="abs hero-title">YOUR COMAPY NAME</div>
  <div class="abs hero-sub narrow">7 DAYS FROM QUOTATION TO DELIVERY USING THE LATEST TECHNOLOGY</div>
  <div class="abs hero-btn narrow">ARCHITECTS &amp; DESIGNERS</div>

  <svg class="abs why" viewBox="0 0 135 455" aria-hidden="true"><polygon points="0,0 135,0 135,423 67.5,455 0,423" fill="#0e2a66"/></svg>
  <div class="abs card why" style="background:none">
    <div class="card-img" role="img" aria-label="Photo of two engineers in hard hats reviewing plans" style="background:linear-gradient(180deg,#7fb3dd,#3c5a7a)"></div>
  </div>
  <div class="abs why-title narrow">WHY<br>US</div>
  <div class="abs why-text narrow">7 Days from quotation to delivery using the latest technology</div>

  <div class="abs card" style="left:229px">
    <div class="card-img" role="img" aria-label="Blue wireframe architectural drawing" style="background:linear-gradient(135deg,#c9cde0,#5a6fd1)"></div>
    <div class="card-title narrow">ARCHITECTS &amp;<br>DESIGNERS</div>
    <div class="card-text narrow">Advice on colours and materials Environmental friendly manufacture</div>
    <svg class="card-arrow" width="13" height="10" viewBox="0 0 13 10"><path d="M0 0l5 5-5 5h3l5-5-5-5zM5 0l5 5-5 5h3l5-5-5-5z" fill="#1f4fb8"/></svg>
  </div>
  <div class="abs card" style="left:374px">
    <div class="card-img" role="img" aria-label="Glasses, calculator and financial papers" style="background:linear-gradient(135deg,#e7ecef,#9fb2c2)"></div>
    <div class="card-title narrow">COMMERCIAL<br>FIT OUR COMPANIES</div>
    <div class="card-text narrow">Site Surveys and Consultation by our experienced design team</div>
    <svg class="card-arrow" width="13" height="10" viewBox="0 0 13 10"><path d="M0 0l5 5-5 5h3l5-5-5-5zM5 0l5 5-5 5h3l5-5-5-5z" fill="#1f4fb8"/></svg>
  </div>
  <div class="abs card" style="left:520px">
    <div class="card-img" role="img" aria-label="Business handshake in an office" style="background:linear-gradient(135deg,#6c7ea0,#1d2535)"></div>
    <div class="card-title narrow">AWARDS &amp;<br>ACCREDITATIONS</div>
    <div class="card-text narrow">We are continually looking at how we can improve our services</div>
    <svg class="card-arrow" width="13" height="10" viewBox="0 0 13 10"><path d="M0 0l5 5-5 5h3l5-5-5-5zM5 0l5 5-5 5h3l5-5-5-5z" fill="#1f4fb8"/></svg>
  </div>

  <div class="abs band"></div>
  <svg class="abs" style="left:81px;top:569px" width="135" height="224" viewBox="0 0 135 224" aria-hidden="true"><polygon points="0,0 135,0 135,192 67.5,224 0,192" fill="#0e2a66"/></svg>
  <ul class="abs checks">
    <li><svg width="10" height="9" viewBox="0 0 10 9"><path d="M1 5l3 3 5-7" stroke="#fff" stroke-width="2" fill="none"/></svg>Loren text here e look for solutions to complex</li>
    <li><svg width="10" height="9" viewBox="0 0 10 9"><path d="M1 5l3 3 5-7" stroke="#fff" stroke-width="2" fill="none"/></svg>Loren&nbsp; involving the funding of capital</li>
    <li><svg width="10" height="9" viewBox="0 0 10 9"><path d="M1 5l3 3 5-7" stroke="#fff" stroke-width="2" fill="none"/></svg>Loren text Equipment</li>
    <li><svg width="10" height="9" viewBox="0 0 10 9"><path d="M1 5l3 3 5-7" stroke="#fff" stroke-width="2" fill="none"/></svg>Loren text ithin an office environment and then</li>
    <li><svg width="10" height="9" viewBox="0 0 10 9"><path d="M1 5l3 3 5-7" stroke="#fff" stroke-width="2" fill="none"/></svg>Lorne textuild documentation around the solution</li>
  </ul>

  <div class="abs project-title narrow">LATEST PROJECT</div>
  <div class="abs project-name">Project Name</div>
  <div class="abs project-text">
    <p>Loren text here e look for solutions to complex problems involving the funding of capital equipment</p>
    <p>Within an office environment and then build documentation around the solution</p>
  </div>
  <svg class="abs" style="left:380px;top:755px" width="13" height="10" viewBox="0 0 13 10"><path d="M0 0l5 5-5 5h3l5-5-5-5zM5 0l5 5-5 5h3l5-5-5-5z" fill="#fff"/></svg>
  <div class="abs project-img" role="img" aria-label="Digital illustration of a glowing blue city skyline"></div>
  <div class="abs dot" style="left:340px;opacity:.45"></div>
  <div class="abs dot" style="left:361px"></div>
  <div class="abs dot" style="left:380px"></div>

  <div class="abs section-title narrow" style="left:87px;top:853px">WHAT PEOPLE SAY ABOUT US</div>
  <div class="abs slider-arrows">&lt; &gt;</div>
  <svg class="abs" style="left:76px;top:905px" width="30" height="24" viewBox="0 0 30 24" aria-hidden="true"><polygon points="0,4 30,0 30,24" fill="#93bf35"/></svg>
  <div class="abs quote"></div>
  <svg class="abs" style="left:111px;top:907px" width="28" height="18" viewBox="0 0 28 18" aria-hidden="true"><g fill="#fff"><circle cx="6" cy="12" r="6"/><path d="M1 11q1-9 9-11l1 2q-5 2-6 8z"/><circle cx="20" cy="12" r="6"/><path d="M15 11q1-9 9-11l1 2q-5 2-6 8z"/></g></svg>
  <div class="abs quote-text">...very efficient dealing with all the necessary paperwork and found me the best deals</div>
  <div class="abs quote-client">Client name<br>USA ...</div>

  <div class="abs section-title narrow" style="left:485px;top:853px">NEWS AND EVENTS</div>
  <div class="abs news-date">11 05 2014</div>
  <div class="abs news-text">We look for solutions to complex problems involving the funding of capital equipment within an office environment and then build documentation around the solution</div>
  <div class="abs read-more">Read More...</div>

  <div class="abs call">Call Us Now 123 456 789</div>

  <div class="abs footer-line"></div>
  <div class="abs footer"></div>
  <nav class="abs footer-nav">
    <span>Home</span><span>About Us</span><span>Services</span><span>Our Clients</span><span>Gallery</span><span>Healty &amp; Safety</span><span>Specification Sheets</span><span>Contact Us</span>
  </nav>
  <div class="abs social">
    <svg width="20" height="20" viewBox="0 0 20 20"><circle cx="10" cy="10" r="10" fill="#fff"/></svg>
    <svg width="20" height="20" viewBox="0 0 20 20"><circle cx="10" cy="10" r="10" fill="#fff"/></svg>
    <svg width="20" height="20" viewBox="0 0 20 20"><circle cx="10" cy="10" r="10" fill="#fff"/></svg>
    <svg width="20" height="20" viewBox="0 0 20 20"><circle cx="10" cy="10" r="10" fill="#fff"/></svg>
    <svg width="20" height="20" viewBox="0 0 20 20"><circle cx="10" cy="10" r="10" fill="#fff"/></svg>
    <svg width="20" height="20" viewBox="0 0 20 20"><circle cx="10" cy="10" r="10" fill="#fff"/><rect x="4.5" y="6" width="11" height="8" fill="#444"/><path d="M4.5 6l5.5 4.5 5.5-4.5" stroke="#fff" stroke-width="1" fill="none"/></svg>
  </div>

  <div class="abs copyright">©&nbsp; your company name here&nbsp; All rights reserved.</div>
</div>
</body>
</html>
```